Industrial Company-Pop-Up Banner Design for Demolition and Infrastructure Company

Hi-
We need to create 2 pop-up banners for our company. They will both have the same logo, but different photos. We would like to have the colors white, red, and black and feature a modern design. I have attached some inspiration photos.

Target Market(s)

Trade Show/Job Fair Audience

Industry/Entity Type

construction, industrial

Font styles to use
Sans Serif

Colors
EB3D1F
EC4F4E
F09395
F8D3D4
FCEDEE

Requirements
Must have
• 2 versions, each with different photos but same design. Logo, Red, Black, and White Color Scheme, Modern Design
Nice to have
• Modern Design similar to the inspiration photos

```html
<!DOCTYPE html>
<html lang="en">
<head>
<meta charset="utf-8">
<title>R.T. Harlan Companies – Pop-Up Banners</title>
<link href="https://fonts.googleapis.com/css2?family=Roboto+Condensed:wght@400;700&display=swap" rel="stylesheet">
<style>
  :root {
    --stage: #e3e2de;
    --charcoal: #2a2a2a;
    --red: #d7191f;
    --white: #ffffff;
  }
  * { margin: 0; padding: 0; box-sizing: border-box; }
  html, body {
    width: 1200px;
    height: 1200px;
    overflow: hidden;
    background: var(--stage);
  }
  .stage {
    position: relative;
    width: 1200px;
    height: 1200px;
  }
  .banner {
    position: absolute;
    top: 40px;
    width: 420px;
    height: 1120px;
    background: var(--charcoal);
    overflow: hidden;
    box-shadow: 0 6px 18px rgba(0,0,0,0.12);
  }
  .banner--one { left: 150px; }
  .banner--two { left: 630px; }
  .banner__art {
    position: absolute;
    inset: 0;
    width: 420px;
    height: 1120px;
  }
  .brand {
    position: absolute;
    left: 0;
    right: 0;
    top: 752px;
    display: flex;
    justify-content: center;
    align-items: center;
    gap: 12px;
    white-space: nowrap;
  }
  .brand__mark {
    width: 26px;
    height: 26px;
    background: var(--red);
    flex: none;
  }
  .brand__name {
    font-family: "Roboto Condensed", sans-serif;
    font-weight: 700;
    color: var(--white);
    font-size: 30px;
    line-height: 1;
    letter-spacing: 0.5px;
  }
  .tagline {
    position: absolute;
    left: 0;
    right: 0;
    top: 842px;
    text-align: center;
    color: var(--white);
    font-family: "Roboto Condensed", sans-serif;
  }
  .tagline__lead {
    font-weight: 700;
    font-size: 22px;
    line-height: 1;
  }
  .tagline__key {
    font-weight: 700;
    font-size: 44px;
    line-height: 1.15;
    margin-top: 2px;
  }
  .tagline__since {
    display: inline-block;
    margin-top: 6px;
    padding: 7px 0 5px 8px;
    border-top: 1.5px solid var(--white);
    border-bottom: 1.5px solid var(--white);
    font-weight: 700;
    font-size: 17px;
    letter-spacing: 8px;
    width: 190px;
  }
  .footer {
    position: absolute;
    left: 0;
    right: 0;
    bottom: 0;
    height: 110px;
    background: var(--red);
    text-align: center;
    padding-top: 22px;
  }
  .footer__web {
    font-family: "Roboto Condensed", sans-serif;
    font-weight: 700;
    font-size: 17px;
    letter-spacing: 5px;
    color: var(--white);
  }
</style>
</head>
<body>
<main class="stage">

  <section class="banner banner--one">
    <svg class="banner__art" viewBox="0 0 420 1120" xmlns="http://www.w3.org/2000/svg">
      <defs>
        <linearGradient id="b1-earthworks" x1="0" y1="0" x2="0" y2="1">
          <stop offset="0" stop-color="#8fb4e0"/>
          <stop offset="0.3" stop-color="#5f7d3e"/>
          <stop offset="1" stop-color="#c79a6e"/>
        </linearGradient>
        <linearGradient id="b1-plant" x1="0" y1="0" x2="0" y2="1">
          <stop offset="0" stop-color="#c9d6e3"/>
          <stop offset="0.45" stop-color="#c6a26a"/>
          <stop offset="0.7" stop-color="#c3382a"/>
          <stop offset="1" stop-color="#6f6354"/>
        </linearGradient>
        <linearGradient id="b1-excavation" x1="0" y1="0" x2="0" y2="1">
          <stop offset="0" stop-color="#dfe8d8"/>
          <stop offset="0.4" stop-color="#c9b07a"/>
          <stop offset="1" stop-color="#9a8462"/>
        </linearGradient>
        <linearGradient id="b1-power" x1="0" y1="0" x2="0" y2="1">
          <stop offset="0" stop-color="#cfd8dc"/>
          <stop offset="0.4" stop-color="#6f7f5c"/>
          <stop offset="0.65" stop-color="#3f8fb6"/>
          <stop offset="1" stop-color="#5a5246"/>
        </linearGradient>
      </defs>
      <polygon class="facet" points="0,760 210,1010 0,1010" fill="#252525"/>
      <polygon class="facet" points="420,700 420,1010 230,1010" fill="#313131"/>
      <polygon class="corner-accent" points="0,11 63,75 0,140" fill="#d7191f"/>
      <polygon role="img" aria-label="Photo: earthmoving site with haul trucks and excavators" points="40,0 398,0 228,193 82,66" fill="url(#b1-earthworks)"/>
      <polygon role="img" aria-label="Photo: excavator demolishing an industrial plant building" points="0,170 82,92 335,354 85,621 0,534" fill="url(#b1-plant)"/>
      <polygon role="img" aria-label="Photo: excavator bucket digging into a rocky cut" points="250,207 420,18 420,409 350,345" fill="url(#b1-excavation)"/>
      <polygon role="img" aria-label="Photo: power plant structures at dusk" points="350,368 420,425 420,598 330,681 190,529" fill="url(#b1-power)"/>
    </svg>
    <div class="brand">
      <span class="brand__mark"></span>
      <span class="brand__name">R.T. HARLAN COMPANIES</span>
    </div>
    <div class="tagline">
      <p class="tagline__lead">Clearing Ground For</p>
      <p class="tagline__key">tomorrow</p>
      <p class="tagline__since">SINCE 1962</p>
    </div>
    <footer class="footer">
      <p class="footer__web">WWW.RTHARLAN.COM</p>
    </footer>
  </section>

  <section class="banner banner--two">
    <svg class="banner__art" viewBox="0 0 420 1120" xmlns="http://www.w3.org/2000/svg">
      <defs>
        <linearGradient id="b2-earthworks" x1="0" y1="0" x2="0" y2="1">
          <stop offset="0" stop-color="#a9c6e8"/>
          <stop offset="0.3" stop-color="#c9a53a"/>
          <stop offset="1" stop-color="#b5562f"/>
        </linearGradient>
        <linearGradient id="b2-assembly" x1="0" y1="0" x2="0" y2="1">
          <stop offset="0" stop-color="#3f72a6"/>
          <stop offset="0.35" stop-color="#dfe3e6"/>
          <stop offset="0.7" stop-color="#c9a94a"/>
          <stop offset="1" stop-color="#6b6a66"/>
        </linearGradient>
        <linearGradient id="b2-excavator" x1="0" y1="0" x2="0" y2="1">
          <stop offset="0" stop-color="#7ea4cf"/>
          <stop offset="0.45" stop-color="#e2c12b"/>
          <stop offset="1" stop-color="#b6532c"/>
        </linearGradient>
        <linearGradient id="b2-teardown" x1="0" y1="0" x2="0" y2="1">
          <stop offset="0" stop-color="#cfe0f0"/>
          <stop offset="0.45" stop-color="#4f78a8"/>
          <stop offset="0.8" stop-color="#8a8782"/>
          <stop offset="1" stop-color="#6d9a3c"/>
        </linearGradient>
      </defs>
      <polygon class="facet" points="0,760 210,1010 0,1010" fill="#252525"/>
      <polygon class="facet" points="420,700 420,1010 230,1010" fill="#313131"/>
      <polygon class="corner-accent" points="0,11 63,75 0,140" fill="#d7191f"/>
      <polygon role="img" aria-label="Photo: haul trucks and excavator on red clay site" points="40,0 398,0 228,193 82,66" fill="url(#b2-earthworks)"/>
      <polygon role="img" aria-label="Photo: long-reach excavator in front of a tall assembly building" points="0,170 82,92 335,354 85,621 0,534" fill="url(#b2-assembly)"/>
      <polygon role="img" aria-label="Photo: yellow excavator on a dirt mound" points="250,207 420,18 420,409 350,345" fill="url(#b2-excavator)"/>
      <polygon role="img" aria-label="Photo: partly demolished blue industrial building" points="350,368 420,425 420,598 330,681 190,529" fill="url(#b2-teardown)"/>
    </svg>
    <div class="brand">
      <span class="brand__mark"></span>
      <span class="brand__name">R.T. HARLAN COMPANIES</span>
    </div>
    <div class="tagline">
      <p class="tagline__lead">Clearing Ground For</p>
      <p class="tagline__key">tomorrow</p>
      <p class="tagline__since">SINCE 1962</p>
    </div>
    <footer class="footer">
      <p class="footer__web">WWW.RTHARLAN.COM</p>
    </footer>
  </section>

</main>
</body>
</html>
```